Looking for a label design for a product call KAVA. My business is to sell prepack kava to stores and online.
I need Hawaiian Polynesian theme around tradition.

The label need to have "Nalu Kava" that's the name of the product. Can add "traditional herbal drink"

Can be colorful, the label will be print in a oval shape clear label size 4.25"x3.25" and will be put on a black back ground.

I don't want any white.

Target Market(s)

Polynesian population and tourist

Industry/Entity Type

Business

Requirements
Must have
• Name: Nalu Kava
inscription: Traditional Herbal drink
inscription: 100% Dried Powder Kava Roots
Net Wt: 8oz
Nice to have
• Traditional art design.

```html
<!DOCTYPE html>
<html lang="en">
<head>
<meta charset="utf-8">
<title>Nalu Kava – Label</title>
<link rel="stylesheet" href="https://fonts.googleapis.com/css2?family=Grandstander:wght@800&family=Cabin:wght@700&family=Roboto+Slab:wght@700&family=Open+Sans:wght@400&display=swap">
<style>
  :root {
    --forest: #004d22;
    --sand: #c2b49c;
    --bark: #6e4a26;
    --mango: #f7941d;
    --mango-light: #fbad1e;
    --sun: #ffec00;
    --ink-slate: #484a5c;
    --ink-grey: #5a5a5a;
  }
  html, body {
    margin: 0;
    padding: 0;
    width: 1200px;
    height: 1200px;
    overflow: hidden;
  }
  .canvas {
    width: 1200px;
    height: 1200px;
    display: flex;
    flex-direction: column;
  }
  .panel {
    width: 1200px;
    height: 600px;
    display: block;
  }
  .panel--forest { background: var(--forest); }
  .panel--sand { background: var(--sand); }
  .label-ring { fill: var(--bark); }
  .label-field { fill: var(--mango); }
  .label-swoosh { fill: none; stroke: var(--mango); stroke-width: 7; stroke-linecap: round; }
  .label-tagline {
    font-family: "Cabin", sans-serif;
    font-weight: 700;
    font-size: 25px;
    fill: var(--sun);
    letter-spacing: 0.5px;
  }
  .label-name {
    font-family: "Grandstander", cursive;
    font-weight: 800;
    font-size: 74px;
    fill: var(--forest);
  }
  .label-desc {
    font-family: "Roboto Slab", serif;
    font-weight: 700;
    font-size: 17px;
    font-variant: small-caps;
    fill: var(--ink-slate);
    letter-spacing: 0.6px;
  }
  .label-weight {
    font-family: "Open Sans", sans-serif;
    font-size: 10px;
    fill: var(--ink-grey);
  }
</style>
</head>
<body>
<main class="canvas">
  <svg class="panel panel--forest" viewBox="0 0 1000 500" xmlns="http://www.w3.org/2000/svg">
    <defs>
      <radialGradient id="field-glow" cx="50%" cy="40%" r="60%">
        <stop offset="0%" stop-color="var(--mango-light)"/>
        <stop offset="100%" stop-color="var(--mango)"/>
      </radialGradient>
      <path id="tagline-arc" d="M 318,192 A 196,128 0 0 1 688,192"/>
      <symbol id="kava-label" viewBox="0 0 1000 500">
        <ellipse class="label-ring" cx="500" cy="250" rx="229" ry="175"/>
        <ellipse class="label-field" cx="500" cy="248" rx="190" ry="124" fill="url(#field-glow)" style="fill:url(#field-glow)" role="img" aria-label="Traditional Polynesian pattern in orange tones"/>
        <path class="label-swoosh" d="M 298,292 Q 312,402 500,402 Q 688,402 702,292"/>
        <text class="label-tagline" text-anchor="middle"><textPath href="#tagline-arc" startOffset="50%">TRADITIONAL HERBAL DRINK</textPath></text>
        <text class="label-name" x="502" y="272" text-anchor="middle">Nalu Kava</text>
        <text class="label-desc" x="500" y="305" text-anchor="middle">100% Dried</text>
        <text class="label-desc" x="500" y="325" text-anchor="middle">Powder Kava Roots</text>
        <text class="label-weight" x="500" y="352" text-anchor="middle">NET WT: 8OZ</text>
      </symbol>
    </defs>
    <use href="#kava-label" x="0" y="0" width="1000" height="500"/>
  </svg>
  <svg class="panel panel--sand" viewBox="0 0 1000 500" xmlns="http://www.w3.org/2000/svg">
    <use href="#kava-label" x="0" y="0" width="1000" height="500"/>
  </svg>
</main>
</body>
</html>
```